Marketing Flyer for Plumber Referals

8.5" x11" Layout should be landscape not portrait. Create a bold, eye-catching flyer that highlights earning potential from referrals for water damage restoration. Use high-contrast colors like blue, yellow, and white, with bold fonts and dynamic layouts. Include images of restoration work, cash, and happy clients. Emphasize key benefits like $500 minimum payouts, fast payments, and unlimited income potential. Keep instructions simple: refer a client, we handle the work, you get paid. Add a clear call-to-action and display contact details prominently. Focus on professionalism and energy.

Target Market(s)

Plumbers and Contractor 8.5" x11" Layout should be landscape not portrait.

Industry/Entity Type

General Contractor

Colors
0054AA
0677BA
7BADD7
CADEEF
E8F1F8
EB3D1F
EC4F4E
F09395
F8D3D4
FCEDEE

Requirements
Must have
• 8.5" x11" Layout should be landscape not portrait.
Nice to have

```html
<!DOCTYPE html>
<html lang="en">
<head>
<meta charset="utf-8">
<title>Flood Referral Flyer</title>
<link href="https://fonts.googleapis.com/css2?family=Merriweather:wght@400;700&display=swap" rel="stylesheet">
<style>
:root{
  --blue-deep:#0054aa;
  --blue:#0a5ec0;
  --blue-mid:#0677ba;
  --blue-light:#7badd7;
  --blue-pale:#cadeef;
  --white:#ffffff;
  --gray-dark:#4a4d52;
  --gray:#8c8f94;
}
*{margin:0;padding:0;box-sizing:border-box}
html,body{width:1200px;height:486px;overflow:hidden;background:var(--white)}
body{position:relative;font-family:"Merriweather",Georgia,serif;color:var(--white)}
.page{position:absolute;top:20px;width:577px;height:446px;overflow:hidden;background:var(--blue)}
.page--front{left:13px}
.page--back{left:604px}
.abs{position:absolute}
.flood-photo{left:0;top:0;width:360px;height:446px;
  background:linear-gradient(90deg,rgba(170,200,230,.9) 0%,rgba(90,140,200,.8) 35%,rgba(10,94,192,0) 100%),
  linear-gradient(180deg,#dfe8f2 0%,#b7c9de 45%,#3d78b8 60%,#1f5aa0 100%)}
.brand{display:flex;align-items:center;gap:5px;font-size:9.5px;letter-spacing:.6px;white-space:nowrap}
.brand-square{width:7px;height:7px;border:1px solid var(--white)}
.headline{font-weight:700;font-size:17px;line-height:25px;letter-spacing:.3px}
.bullet{display:flex;align-items:center;gap:4px;font-size:10px}
.bullet svg{width:9px;height:9px}
.section-title{font-weight:700;font-size:16px}
.benefit{display:flex;gap:10px;width:165px}
.benefit-icon{flex:none;width:38px;height:38px}
.benefit h3{font-size:10.5px;font-weight:700;margin-top:4px;margin-bottom:3px;white-space:nowrap}
.benefit p{font-size:7.8px;line-height:11.5px}
.tagline{font-weight:700;font-size:13.5px;letter-spacing:.2px}
.pipe-photo{left:0;top:0;width:577px;height:446px;
  background:radial-gradient(ellipse at 45% 45%,#f4f6f8 0%,#c9ccd1 22%,#6d7177 55%,#3b3e43 100%)}
.blue-band{left:0;top:0;width:577px;height:446px}
.back-title{font-weight:700;font-size:16px;letter-spacing:.3px;white-space:nowrap}
.link-title{font-weight:700;font-size:12px;text-decoration:underline;text-underline-offset:2px}
.step{display:flex;align-items:flex-start}
.step-icon{position:absolute;width:40px;height:40px;border-radius:50%;background:var(--white)}
.step-text h3{font-size:11px;font-weight:700;margin-bottom:4px;white-space:nowrap}
.step-text p{font-size:8px;line-height:11.5px}
.cta{font-weight:700;font-size:13.5px;text-decoration:underline;text-underline-offset:2px;white-space:nowrap}
.contact{display:flex;align-items:center;gap:7px;font-size:9.5px;font-weight:700}
.contact svg{width:12px;height:12px}
</style>
</head>
<body>

<section class="page page--front">
  <div class="abs flood-photo" role="img" aria-label="Flooded home interior with staircase and standing water"></div>

  <div class="abs brand" style="left:250px;top:68px"><span class="brand-square"></span>HARBOR COAST REMODEL</div>

  <h1 class="abs headline" style="left:245px;top:136px">EARN UNLIMITED CASH<br>GET PAID TO REFER A FLOOD</h1>

  <div class="abs bullet" style="left:245px;top:194px">
    <svg viewBox="0 0 10 10"><circle cx="5" cy="5" r="5" fill="#fff"/><path d="M3 5h4M5.2 3l2 2-2 2" stroke="#0a5ec0" stroke-width="1.3" fill="none"/></svg>
    $500 Minimum or 10% Per Referral!
  </div>
  <div class="abs bullet" style="left:245px;top:215px">
    <svg viewBox="0 0 10 10"><circle cx="5" cy="5" r="5" fill="#fff"/><path d="M3 5h4M5.2 3l2 2-2 2" stroke="#0a5ec0" stroke-width="1.3" fill="none"/></svg>
    Partner with the #1 Water Damage Restoration Team
  </div>

  <h2 class="abs section-title" style="left:245px;top:243px">Why Partner with Us?</h2>

  <div class="abs benefit" style="left:245px;top:281px">
    <svg class="benefit-icon" viewBox="0 0 38 38"><circle cx="19" cy="19" r="18" fill="none" stroke="#fff" stroke-dasharray="3 2"/><circle cx="19" cy="17" r="7" fill="none" stroke="#fff" stroke-width="1.5"/><path d="M15.5 17l2.5 2.5 4.5-5" stroke="#fff" stroke-width="1.5" fill="none"/><path d="M15 23l-2 6 3-1 2 2 1-5M23 23l2 6-3-1-2 2" stroke="#fff" fill="none"/></svg>
    <div><h3>Guaranteed Payout:</h3><p>Minimum $500 or 10% of the invoice, paid fast.</p></div>
  </div>
  <div class="abs benefit" style="left:404px;top:281px">
    <svg class="benefit-icon" viewBox="0 0 38 38"><circle cx="19" cy="19" r="18" fill="none" stroke="#fff" stroke-dasharray="3 2"/><rect x="11" y="10" width="12" height="17" fill="none" stroke="#fff" stroke-width="1.5"/><path d="M13.5 14h7M13.5 18h5" stroke="#fff"/><circle cx="23" cy="23" r="4" fill="none" stroke="#fff" stroke-width="1.5"/><path d="M26 26l3 3" stroke="#fff" stroke-width="1.5"/></svg>
    <div><h3>Free Evaluations:</h3><p>We assess damage and process insurance claims for your clients.</p></div>
  </div>
  <div class="abs benefit" style="left:245px;top:343px">
    <svg class="benefit-icon" viewBox="0 0 38 38"><circle cx="19" cy="19" r="18" fill="none" stroke="#fff" stroke-dasharray="3 2"/><circle cx="19" cy="12" r="3" fill="#fff"/><path d="M13 20h12v3H13z" fill="#fff"/><path d="M10 22l4 6h10l4-6" stroke="#fff" stroke-width="1.8" fill="none"/></svg>
    <div><h3>Industry Leaders</h3><p>Certified experts with 24/7 rapid response.</p></div>
  </div>
  <div class="abs benefit" style="left:404px;top:343px">
    <svg class="benefit-icon" viewBox="0 0 38 38"><circle cx="19" cy="19" r="18" fill="none" stroke="#fff" stroke-dasharray="3 2"/><circle cx="19" cy="15" r="6" fill="none" stroke="#fff" stroke-width="1.5"/><text x="19" y="18.5" font-size="9" font-weight="700" fill="#fff" text-anchor="middle" font-family="Merriweather,serif">$</text><path d="M10 26q4-3 8 0h6l3-2" stroke="#fff" stroke-width="1.5" fill="none"/></svg>
    <div><h3>Affordable Solutions:</h3><p>Lowest out-of-pocket costs for your customers.</p></div>
  </div>

  <p class="abs tagline" style="left:245px;top:405px">Send Referrals. Get Paid. Grow Your Business.</p>
</section>

<section class="page page--back">
  <div class="abs pipe-photo" role="img" aria-label="White drain pipe under a sink leaking water"></div>
  <svg class="abs blue-band" viewBox="0 0 577 446" preserveAspectRatio="none" aria-hidden="true">
    <polygon points="309,0 577,0 577,446 223,446" fill="#0a5ec0"/>
  </svg>

  <div class="abs brand" style="left:318px;top:68px"><span class="brand-square"></span>HARBOR COAST REMODEL</div>

  <h1 class="abs back-title" style="left:308px;top:114px">GET PAID TO REFER A FLOOD</h1>
  <h2 class="abs link-title" style="left:308px;top:150px">How It Works</h2>

  <div class="abs step-icon" style="left:256px;top:164px">
    <svg viewBox="0 0 40 40"><path d="M13 14h6v8h8v6" stroke="#0a5ec0" stroke-width="2.2" fill="none"/><path d="M26 12v5" stroke="#0a5ec0" stroke-width="2"/></svg>
  </div>
  <div class="abs step-text" style="left:306px;top:188px">
    <h3>Refer Flood, Water and Mold Damage</h3><p>Call, book online, or text us directly.</p>
  </div>

  <div class="abs step-icon" style="left:245px;top:220px">
    <svg viewBox="0 0 40 40"><rect x="13" y="11" width="13" height="17" fill="none" stroke="#0a5ec0" stroke-width="1.5"/><path d="M15 15l1.5 1.5 3-3M15 21l1.5 1.5 3-3" stroke="#0a5ec0" stroke-width="1.2" fill="none"/><path d="M24 26l5-8" stroke="#0a5ec0" stroke-width="1.5"/></svg>
  </div>
  <div class="abs step-text" style="left:295px;top:244px">
    <h3>We Take Care of Everything</h3><p>Free evaluations, insurance claims, and professional service.</p>
  </div>

  <div class="abs step-icon" style="left:235px;top:272px">
    <svg viewBox="0 0 40 40"><circle cx="20" cy="20" r="10" fill="none" stroke="#0a5ec0" stroke-width="1.3" stroke-dasharray="2 1.5"/><text x="20" y="23" font-size="6.5" font-weight="700" fill="#0a5ec0" text-anchor="middle" font-family="Merriweather,serif">PAID</text></svg>
  </div>
  <div class="abs step-text" style="left:284px;top:296px">
    <h3>Get Paid Fast</h3><p>o $500 minimum or 10% of the invoice within 48 hours of final<br>payment.</p>
  </div>

  <h2 class="abs cta" style="left:281px;top:352px">Call Text or Book On-line</h2>

  <div class="abs contact" style="left:282px;top:383px">
    <svg viewBox="0 0 12 12"><path d="M2.5 1l2 2.5-1.2 1.3q1.2 2.5 3.7 3.7L8.3 7.3l2.5 2-1.3 1.7Q3 10.5 1 2.3z" fill="#fff"/></svg>
    555-014-2290
  </div>
  <div class="abs contact" style="left:282px;top:403px">
    <svg viewBox="0 0 12 12"><rect x="0.5" y="2" width="11" height="8" fill="#fff"/><path d="M0.5 2.5l5.5 4 5.5-4" stroke="#0a5ec0" fill="none"/></svg>
    HarborCoastBuild.com
  </div>
</section>

</body>
</html>
```